Website Revamp for 7K Distributor

Brovin Pte Ltd (http://brovin.com.sg/about.php) is a 7K authorized distributor located in Singapore.

The revamp hopes to move the look & feel of the website from a corporate/industrial feel to one that is more homely/interior-design, so as to attract architects, home-builders, interior-designers with a more up-market design.
Updates

If product images are required, please use images from www.brovin.com.sg. Thanks!

For newsletter signup, just a link at the header will do, as we will be implementing additional profiling fields in the signup form.

Target Market(s)

Hopes to attract architects, home-builders, interior-designers with a more up-market design.

Industry/Entity Type

Industrial

Requirements
Must have
• Refer to brief document

```html
<!DOCTYPE html>
<html lang="en">
<head>
<meta charset="utf-8">
<title>Brovin – Window Film Solutions</title>
<link href="https://fonts.googleapis.com/css2?family=Roboto+Condensed:wght@400;700&family=Roboto:wght@300;400&display=swap" rel="stylesheet">
<style>
:root{
  --header-bg:#242424;
  --brand-blue:#1c8ad6;
  --link-blue:#2f95d8;
  --accent-red:#d00a0a;
  --accent-red-dark:#a80303;
  --linen:#e4e4e4;
  --ink:#222;
  --body-text:#555;
  --white:#fff;
  --rule:#ececec;
}
*{margin:0;padding:0;box-sizing:border-box}
html,body{width:1200px;height:1040px;overflow:hidden;background:var(--white)}
body{position:relative;font-family:"Roboto",Arial,sans-serif;color:var(--ink)}
.abs{position:absolute}

/* header */
.site-header{left:0;top:0;width:1200px;height:63px;background:var(--header-bg);box-shadow:0 2px 4px rgba(0,0,0,.35);z-index:5}
.brand{left:117px;top:8px;font:700 44px/46px "Roboto Condensed",sans-serif;color:var(--brand-blue);letter-spacing:1px}
.main-nav a{position:absolute;top:21px;font:700 18px/22px "Roboto Condensed",sans-serif;color:var(--white);text-decoration:none}
.main-nav .is-current{color:var(--link-blue)}
.main-nav .is-open{left:695px;top:15px;width:125px;height:33px;border-radius:17px;background:var(--accent-red);border:1px solid #ff3b3b;padding-top:6px;text-align:center}

/* dropdown */
.dropdown{left:694px;top:60px;width:201px;height:159px;border-radius:0 10px 12px 12px;background:linear-gradient(#dc0606,#b10202);border:1px solid #ff2a2a;box-shadow:0 3px 6px rgba(0,0,0,.35);z-index:6}
.dropdown::before{content:"";position:absolute;left:30px;top:-8px;border:7px solid transparent;border-bottom-color:var(--accent-red);border-top:0}
.dropdown .row-active{position:absolute;left:0;top:12px;width:200px;height:22px;background:rgba(0,0,0,.18)}
.dropdown a,.submenu a{position:absolute;left:14px;font:700 14px/16px "Roboto Condensed",sans-serif;color:var(--white);text-decoration:none}
.submenu{left:894px;top:70px;width:154px;height:67px;border-radius:0 10px 10px 10px;background:linear-gradient(#dc0606,#b10202);border:1px solid #ff2a2a;box-shadow:0 3px 6px rgba(0,0,0,.35);z-index:6}
.submenu .row-active{position:absolute;left:0;top:4px;width:153px;height:21px;background:rgba(0,0,0,.18)}

/* hero */
.hero-band{left:0;top:63px;width:1200px;height:415px;background:repeating-linear-gradient(90deg,#e9e9e9 0 2px,#dedede 2px 3px),var(--linen)}
.hero-frame{left:117px;top:104px;width:960px;height:352px;background:var(--white);box-shadow:0 2px 6px rgba(0,0,0,.15)}
.hero-photo{left:128px;top:116px;width:938px;height:328px;background:linear-gradient(135deg,#0c1c4a 0%,#1e4f9c 35%,#7fb3e6 55%,#1f5fa8 75%,#0b2a5e 100%)}
.hero-caption{left:128px;top:384px;width:938px;height:60px;background:rgba(30,32,40,.72);color:var(--white);font:400 14px/60px "Roboto",sans-serif;padding-left:16px}
.hero-caption b{font-weight:700;font-family:"Roboto Condensed",sans-serif;font-size:15px}
.slider-dots span{position:absolute;top:405px;width:20px;height:20px;border-radius:50%;background:#333}
.slider-dots .is-active{background:#111;border:2px solid var(--link-blue)}

.tab{top:456px;height:42px;width:183px;font:700 19px/42px "Roboto Condensed",sans-serif;text-align:center;box-shadow:0 3px 5px rgba(0,0,0,.3)}
.tab-products{left:403px;background:linear-gradient(#333,#000);color:var(--white)}
.tab-portfolio{left:590px;background:linear-gradient(#fafafa,#e2e2e2);color:var(--ink)}

/* content */
.section-title{font:300 30px/36px "Roboto",sans-serif;color:var(--ink)}
.section-title em{font-style:normal;color:var(--accent-red)}
.card{width:200px}
.card-photo{width:199px;height:137px;border:1px solid #ccc;box-shadow:0 8px 8px -6px rgba(0,0,0,.35)}
.card h3{margin-top:18px;font:400 14px/20px "Roboto",sans-serif;color:#333}
.card p{margin-top:9px;font:400 11px/20px "Roboto",sans-serif;color:var(--body-text)}
.card a{display:block;margin-top:5px;font:400 11px/16px "Roboto",sans-serif;color:var(--accent-red);text-decoration:none}

.sidebar-rule{left:812px;top:545px;width:4px;height:355px;background:linear-gradient(90deg,#ddd,#fff)}
.subscribe-sub{left:836px;top:580px;font:400 14px/18px "Roboto",sans-serif;color:#333}
.email-field{left:836px;top:614px;width:230px;height:34px;border:1px solid #ccc;border-top:2px solid #bbb;border-radius:3px;font:italic 300 14px/32px "Roboto",sans-serif;color:#aaa;padding-left:11px}
.submit-btn{left:889px;top:666px;width:116px;height:33px;border-radius:17px;background:linear-gradient(#e81212,#b40000);color:var(--white);font:700 19px/33px "Roboto Condensed",sans-serif;text-align:center}
.partner-name{left:843px;top:722px;font:400 22px/24px "Roboto Condensed",sans-serif;color:#111}
.partner-text{left:843px;top:754px;font:400 16px/16px "Roboto Condensed",sans-serif;color:#111;letter-spacing:-.3px}
.association-badge{left:845px;top:812px;width:198px;height:46px;background:#1a1a1a;border-radius:3px}

/* footer */
.footer-rule{left:128px;top:963px;width:939px;height:5px;background:var(--rule)}
.copyright{left:129px;top:987px;font:400 11px/14px "Roboto",sans-serif;color:#444}
.footer-nav a{position:absolute;top:987px;font:400 11px/14px "Roboto",sans-serif;color:#444;text-decoration:none}
.footer-nav .is-current{color:var(--link-blue)}
</style>
</head>
<body>

<header class="abs site-header">
  <div class="abs brand">BROVIN</div>
  <nav class="main-nav">
    <a style="left:468px">Home</a>
    <a class="is-current" style="left:555px">The Philosophy</a>
    <a class="is-open">Our Solutions</a>
    <a style="left:852px">Our Portfolios</a>
    <a style="left:998px">Contact Us</a>
  </nav>
</header>

<section class="abs hero-band"></section>
<div class="abs hero-frame"></div>
<div class="abs hero-photo" role="img" aria-label="Glass office tower facade photographed from below against a blue sky"></div>
<div class="abs hero-caption"><b>Morbi dapibus</b> mauris nec nunc facilisis vitae posuere massa faucibus.</div>
<div class="slider-dots">
  <span style="left:931px"></span><span style="left:959px"></span><span class="is-active" style="left:987px"></span><span style="left:1012px"></span>
</div>

<div class="abs tab tab-products">Featured Products</div>
<div class="abs tab tab-portfolio">Featured Portfolio</div>

<nav class="abs dropdown">
  <span class="row-active"></span>
  <a style="top:16px">Glass &amp; Glazing</a>
  <a style="top:44px">Building Services</a>
  <a style="top:72px">Filtration</a>
  <a style="top:100px">Automotives</a>
  <a style="top:128px">Others</a>
</nav>
<nav class="abs submenu">
  <span class="row-active"></span>
  <a style="left:12px;top:7px">Sun Control Films</a>
  <a style="left:12px;top:35px">Safety Films</a>
</nav>

<h2 class="abs section-title" style="left:130px;top:546px">What’s <em>hot?</em></h2>

<article class="abs card" style="left:129px;top:606px">
  <div class="card-photo" role="img" aria-label="Sunny living room with white sofa and tall windows" style="background:linear-gradient(160deg,#f3e5bf,#d9b98a 60%,#8c5a33)"></div>
  <h3>Lorem Ipsum</h3>
  <p>Etiam eros sem, viverra non placerat eget, ullamcorper nec leo. Proin quis tortor a ante convallis</p>
  <a>Read More</a>
</article>
<article class="abs card" style="left:354px;top:606px">
  <div class="card-photo" role="img" aria-label="Modern glass office building with palm trees" style="background:linear-gradient(120deg,#7ea6c9,#c9cfd6 50%,#b89aa2 75%,#4d6b3c)"></div>
  <h3>Lorem Ipsum</h3>
  <p>Etiam eros sem, viverra non placerat eget, ullamcorper nec leo. Proin quis tortor a ante convallis</p>
  <a>Read More</a>
</article>
<article class="abs card" style="left:582px;top:606px">
  <div class="card-photo" role="img" aria-label="Spacious lounge with white sofas and large paned windows" style="background:linear-gradient(170deg,#4a3a2c,#a89480 45%,#e8e2da 75%,#6b5a4a)"></div>
  <h3>Lorem Ipsum</h3>
  <p>Etiam eros sem, viverra non placerat eget, ullamcorper nec leo. Proin quis tortor a ante convallis</p>
  <a>Read More</a>
</article>

<aside>
  <div class="abs sidebar-rule"></div>
  <h2 class="abs section-title" style="left:835px;top:546px">Subscribe</h2>
  <div class="abs subscribe-sub">for a newsletter</div>
  <div class="abs email-field">Email Address</div>
  <div class="abs submit-btn">SUBMIT</div>
  <div class="abs partner-name">7K</div>
  <div class="abs partner-text">Authorized Distributor<br>Architectural and Interior Solutions</div>
  <div class="abs association-badge" role="img" aria-label="Industry association membership badge"></div>
</aside>

<footer>
  <div class="abs footer-rule"></div>
  <div class="abs copyright">© Copyright 2010 Brovin Pte Ltd. All Rights Reserved.</div>
  <nav class="footer-nav">
    <a style="left:697px">The Philosophy</a>
    <a class="is-current" style="left:790px">Our Solutions</a>
    <a style="left:872px">Our Portfolios</a>
    <a style="left:954px">Contact Us</a>
    <a style="left:1023px">Site Map</a>
  </nav>
</footer>

</body>
</html>
```